Hi,

I would like to create a beer label for our new beer we are creating,

We are called "The Larkmoor Brewing Co."

Our new beer is called "The Brass Lantern" which is a "Pale Ale" with an "ABV 4.8%"

our tag line is "Built For Sessionability"

Everything writen in inverted comma's I would like on the label

I would like it to be a round beer label as well with some sort of picture in the background.

This is our first design of any kind for the company so we do not have a logo or any designs so its open to anything. I would like it to be new and trendy with an older style feel to it.

Industry/Entity Type

Graphic Design

Requirements
Must have
• Round so I can convert into a beer coaster,
needs to have alcohol percentage.

```html
<!DOCTYPE html>
<html lang="en">
<head>
<meta charset="utf-8">
<title>The Brass Lantern – Pale Ale Label</title>
<link rel="stylesheet" href="https://fonts.googleapis.com/css2?family=Federo&family=Merriweather:wght@400;900&display=swap">
<style>
  :root {
    --tan: #c3b170;
    --maroon: #761c14;
    --rust: #a8452a;
    --page: #ffffff;
  }
  html, body {
    margin: 0;
    padding: 0;
    width: 1200px;
    height: 1200px;
    overflow: hidden;
    background: var(--page);
  }
  .label {
    display: block;
    width: 1200px;
    height: 1200px;
  }
  .label-disc { fill: var(--tan); }
  .ring-outer { fill: none; stroke: var(--maroon); stroke-width: 9; }
  .ring-inner { fill: none; stroke: var(--rust); stroke-width: 5; }
  .ring-line { fill: none; stroke: var(--maroon); stroke-width: 3; }
  .star { fill: var(--maroon); }
  .frame-band { fill: var(--tan); stroke: var(--maroon); stroke-width: 18; }
  .frame-band-core { fill: none; stroke: var(--rust); stroke-width: 9; }
  .frame-inner { fill: none; stroke: var(--maroon); stroke-width: 3; }
  .beer-name, .tagline, .style-name {
    font-family: "Merriweather", Georgia, serif;
    font-weight: 900;
    fill: var(--maroon);
    text-anchor: middle;
  }
  .beer-name { font-size: 38px; }
  .tagline { font-size: 32px; }
  .style-name { font-size: 44px; }
  .abv {
    font-family: "Merriweather", Georgia, serif;
    font-weight: 400;
    font-size: 18px;
    fill: var(--maroon);
    text-anchor: middle;
  }
  .brewery {
    font-family: "Federo", "Poiret One", sans-serif;
    font-weight: 400;
    fill: var(--maroon);
  }
  .brewery-the { font-size: 54px; }
  .brewery-name { font-size: 168px; }
  .brewery-sub { font-size: 56px; text-anchor: middle; }
</style>
</head>
<body>
<svg class="label" viewBox="0 0 823 823" xmlns="http://www.w3.org/2000/svg" role="img" aria-label="Round beer label for The Brass Lantern pale ale by The Larkmoor Brewing Co.">
  <circle class="label-disc" cx="411.5" cy="411.5" r="411"/>
  <circle class="ring-outer" cx="411.5" cy="411.5" r="394"/>
  <circle class="ring-inner" cx="411.5" cy="411.5" r="386"/>
  <circle class="ring-line" cx="411.5" cy="411.5" r="380"/>

  <g class="stars">
    <polygon class="star" points="322,58 331,86 361,86 337,103 346,131 322,114 298,131 307,103 283,86 313,86"/>
    <polygon class="star" points="411.5,58 420.5,86 450.5,86 426.5,103 435.5,131 411.5,114 387.5,131 396.5,103 372.5,86 402.5,86"/>
    <polygon class="star" points="501,58 510,86 540,86 516,103 525,131 501,114 477,131 486,103 462,86 492,86"/>
  </g>

  <text class="beer-name" x="411.5" y="200" textLength="520" lengthAdjust="spacingAndGlyphs">THE BRASS LANTERN</text>

  <g class="frame">
    <path class="frame-band" d="M92,226 H731 A42 42 0 0 0 773,268 V564 A42 42 0 0 0 731,606 H92 A42 42 0 0 0 50,564 V268 A42 42 0 0 0 92,226 Z"/>
    <path class="frame-band-core" d="M92,226 H731 A42 42 0 0 0 773,268 V564 A42 42 0 0 0 731,606 H92 A42 42 0 0 0 50,564 V268 A42 42 0 0 0 92,226 Z"/>
    <path class="frame-inner" d="M96,240 H727 A32 32 0 0 0 759,272 V560 A32 32 0 0 0 727,592 H96 A32 32 0 0 0 64,560 V272 A32 32 0 0 0 96,240 Z"/>
  </g>

  <g class="brewery">
    <text class="brewery brewery-the" x="192" y="348">THE</text>
    <text class="brewery brewery-name" x="110" y="478" textLength="604" lengthAdjust="spacingAndGlyphs">LARKMOOR</text>
    <text class="brewery brewery-sub" x="411.5" y="540">BREWING CO.</text>
  </g>

  <text class="tagline" x="411.5" y="645" textLength="530" lengthAdjust="spacingAndGlyphs">BUILT FOR SESSIONABILITY</text>
  <text class="style-name" x="411.5" y="717" textLength="232" lengthAdjust="spacingAndGlyphs">PALE ALE</text>
  <text class="abv" x="411.5" y="766">ABV 4.8%</text>
</svg>
</body>
</html>
```